Harbel Shipping

A flyer that sells both air and sea freight services. We had an attempt at this and wanted a fresh concept from your designers. Colors should be vibrant and the text readable on a digital billboard as well. Our attempt is attached along with our logo file.

Designers***The contents on our attempt flyer should be applied to your flyer design.

Thanks!

Industry/Entity Type

Shipping

```html
<!DOCTYPE html>
<html lang="en">
<head>
<meta charset="utf-8">
<title>Harbel Shipping – Flyer</title>
<link rel="stylesheet" href="https://fonts.googleapis.com/css2?family=Montserrat:wght@700;800;900&family=Roboto+Condensed:wght@400;700&display=swap">
<style>
  :root {
    --red: #c61f26;
    --navy: #332f85;
    --white: #ffffff;
    --ink: #2b2b2b;
    --sky-light: #f2f8fd;
    --sky: #b9daf0;
    --page: #e6e6e6;
    --footer: #f4f4f4;
  }
  * { margin: 0; padding: 0; box-sizing: border-box; }
  html, body { width: 1200px; height: 900px; overflow: hidden; }
  body { background: var(--page); position: relative; font-family: "Montserrat", sans-serif; }

  .flyer {
    position: absolute; left: 300px; top: 25px;
    width: 600px; height: 850px;
    background: var(--footer); overflow: hidden;
    box-shadow: 0 6px 18px rgba(0,0,0,.18);
  }
  .hero-photo {
    position: absolute; left: 0; top: 0; width: 600px; height: 552px;
    background: linear-gradient(180deg,
      var(--sky-light) 0%, #d9ebf7 30%, var(--sky) 62%,
      #b4705a 70%, #c7643c 76%, #3e4a5a 84%, #2a3340 89%, #3c7fa0 93%, #4a90b0 100%);
  }
  .hero-photo::before {
    content: ""; position: absolute; inset: 0;
    background: linear-gradient(115deg, rgba(255,255,255,.95) 0%, rgba(255,255,255,.6) 35%, rgba(255,255,255,0) 60%);
  }
  .headline {
    position: absolute; left: 41px; top: 28px;
    font-weight: 900; font-size: 98px; line-height: 78px; letter-spacing: -1px;
  }
  .headline span { display: block; }
  .headline .red { color: var(--red); }
  .headline .navy { color: var(--navy); }

  .brand {
    position: absolute; left: 468px; top: 30px; width: 110px;
    text-align: center; color: var(--red);
    font-weight: 800; font-size: 19px; line-height: 20px;
  }
  .brand .mark {
    display: block; width: 64px; height: 64px; margin: 0 auto 10px;
    border-radius: 50%; background: var(--red);
  }

  .offer-panel { position: absolute; left: 0; top: 550px; width: 600px; height: 300px; }
  .offer-tab {
    position: absolute; left: 0; top: 551px; width: 213px; height: 42px;
    background: var(--navy); border-bottom-right-radius: 30px;
    color: var(--white); font-weight: 800; font-size: 18px;
    padding: 10px 0 0 45px;
  }
  .services {
    position: absolute; left: 48px; top: 605px; width: 540px;
    list-style: none; display: grid; grid-template-columns: 244px 1fr; row-gap: 6px;
    color: var(--white); font-weight: 800; font-size: 19px; line-height: 22px;
  }
  .services li { display: flex; align-items: center; gap: 6px; }
  .services svg { width: 14px; height: 14px; flex: none; }

  .phone {
    position: absolute; left: 0; top: 700px; width: 600px;
    display: flex; justify-content: center; align-items: center; gap: 12px;
    color: var(--white); font-weight: 800; font-size: 62px; letter-spacing: 2px;
  }
  .phone svg { width: 46px; height: 46px; }

  .footer-note {
    position: absolute; left: 20px; top: 805px;
    font-family: "Roboto Condensed", sans-serif; color: var(--ink);
  }
  .footer-note p { font-size: 13px; line-height: 17px; }
  .footer-note .web { font-weight: 700; font-size: 14px; letter-spacing: .3px; }
  .address {
    position: absolute; right: 21px; top: 822px;
    font-family: "Roboto Condensed", sans-serif; font-weight: 700; font-size: 14px;
    color: var(--ink); letter-spacing: .3px;
  }
  .social { position: absolute; left: 521px; top: 790px; display: flex; gap: 10px; }
  .social span { width: 20px; height: 20px; background: var(--ink); border-radius: 4px; }
</style>
</head>
<body>
  <main class="flyer">
    <div class="hero-photo" role="img" aria-label="Photo of a passenger jet flying over a container ship loaded with colourful containers at a port crane, under a blue sky"></div>

    <h1 class="headline">
      <span class="red">SAVE</span>
      <span class="red">MONEY</span>
      <span class="navy">SHIP</span>
      <span class="navy">BETTER</span>
    </h1>

    <div class="brand"><span class="mark"></span>HARBEL SHIPPING</div>

    <svg class="offer-panel" viewBox="0 0 600 300" aria-hidden="true">
      <path d="M0 0 H600 V187 Q300 262 0 187 Z" fill="var(--red)"/>
    </svg>

    <div class="offer-tab">WE OFFER:</div>

    <ul class="services">
      <li><svg viewBox="0 0 14 14"><path d="M1 7.5 L5 11.5 L13 2" fill="none" stroke="#fff" stroke-width="1.6"/></svg>CARGO</li>
      <li><svg viewBox="0 0 14 14"><path d="M1 7.5 L5 11.5 L13 2" fill="none" stroke="#fff" stroke-width="1.6"/></svg>SEA FREIGHT</li>
      <li><svg viewBox="0 0 14 14"><path d="M1 7.5 L5 11.5 L13 2" fill="none" stroke="#fff" stroke-width="1.6"/></svg>CONSOLIDATION</li>
      <li><svg viewBox="0 0 14 14"><path d="M1 7.5 L5 11.5 L13 2" fill="none" stroke="#fff" stroke-width="1.6"/></svg>CUSTOMS CLEARANCE</li>
      <li><svg viewBox="0 0 14 14"><path d="M1 7.5 L5 11.5 L13 2" fill="none" stroke="#fff" stroke-width="1.6"/></svg>AIR FREIGHT</li>
      <li><svg viewBox="0 0 14 14"><path d="M1 7.5 L5 11.5 L13 2" fill="none" stroke="#fff" stroke-width="1.6"/></svg>TRUCKING</li>
    </ul>

    <div class="phone">
      <svg viewBox="0 0 46 46" aria-hidden="true">
        <circle cx="23" cy="23" r="23" fill="#fff"/>
        <path d="M16 12 L20 12 L22 18 L19 21 Q21 26 26 28 L29 25 L35 27 L35 31 Q35 34 31 34 Q14 33 12 16 Q12 12 16 12 Z" fill="var(--red)"/>
      </svg>
      <span>390-2716</span>
    </div>

    <div class="footer-note">
      <p>Sign up to receive your suite#</p>
      <p class="web">WWW.HARBELSHIPPINGBAHAMAS.COM</p>
    </div>
    <div class="social" aria-hidden="true"><span></span><span></span></div>
    <p class="address"># 42 SEABREEZE AVE. NASSAU, BAHAMAS</p>
  </main>
</body>
</html>
```